all sorted property services

Target Market(s)

General letter head for emails and letter quotes ect

Colors
0054AA
0677BA
7BADD7
CADEEF
E8F1F8
0094D4
00A9DD
6FCCEA
C7EBF8
E9F6FB

Requirements
Must have
• logo phone email website names
Nice to have
• what we do (from the website)

```html
<!DOCTYPE html>
<html lang="en">
<head>
<meta charset="utf-8">
<title>All Sorted Property Services – Letterhead</title>
<link rel="stylesheet" href="https://fonts.googleapis.com/css2?family=Arimo:wght@400;700&family=Montserrat:wght@700;800&display=swap">
<style>
  :root {
    --brand-blue: #0054AA;
    --ocean: #0677BA;
    --soft-blue: #7BADD7;
    --mist: #CADEEF;
    --text: #2b2b2b;
    --muted: #444;
    --backdrop: #e4e4e4;
    --paper: #ffffff;
  }
  * { box-sizing: border-box; margin: 0; padding: 0; }
  html, body { width: 1200px; height: 960px; overflow: hidden; }
  body {
    background: var(--backdrop);
    font-family: "Arimo", Arial, sans-serif;
    color: var(--text);
  }
  .letterhead {
    position: absolute;
    left: 282px; top: 30px;
    width: 636px; height: 900px;
    background: var(--paper);
    overflow: hidden;
  }
  .letterhead__corners { position: absolute; inset: 0; width: 100%; height: 100%; }

  .brand {
    position: absolute; left: 30px; top: 176px;
    display: flex; align-items: center; gap: 10px;
  }
  .brand__dot {
    width: 38px; height: 38px; border-radius: 50%;
    background: var(--brand-blue);
    flex: none;
  }
  .brand__name {
    font-family: "Montserrat", Arial, sans-serif;
    font-weight: 800;
    color: var(--brand-blue);
    line-height: 1.1;
  }
  .brand__name-main { display: block; font-size: 22px; letter-spacing: 0.5px; }
  .brand__name-sub { display: block; font-size: 9px; letter-spacing: 2.6px; }

  .contact {
    position: absolute; left: 440px; top: 86px;
    border-left: 1px solid var(--muted);
    padding-left: 9px;
    font-style: normal;
    font-size: 9.5px; line-height: 1.4; color: var(--muted);
  }
  .contact__item { display: flex; align-items: center; gap: 4px; }
  .contact__icon { width: 8px; height: 8px; fill: var(--ocean); flex: none; }

  .letter { position: absolute; left: 78px; top: 262px; width: 470px; }
  .letter__greeting {
    font-family: "Montserrat", Arial, sans-serif;
    font-weight: 700; font-size: 15px; color: #333;
    margin-bottom: 18px;
  }
  .letter__para { font-size: 11px; line-height: 1.42; margin-bottom: 17px; color: var(--muted); }
  .letter__closing { font-size: 10px; font-weight: 700; margin-top: 24px; color: #333; }
  .letter__signature {
    width: 130px; height: 40px; margin: 18px 0 0 40px;
    border-radius: 20px;
    background: linear-gradient(90deg, #ececec, #f6f6f6);
  }
</style>
</head>
<body>
  <main class="letterhead">
    <svg class="letterhead__corners" viewBox="0 0 636 900" aria-hidden="true">
      <defs>
        <linearGradient id="corner-fill" x1="0" y1="0" x2="1" y2="1">
          <stop offset="0" stop-color="#0054AA"/>
          <stop offset="1" stop-color="#0677BA"/>
        </linearGradient>
      </defs>
      <g class="corner corner--top">
        <path d="M0,0 H560 C360,30 130,80 0,170 Z" fill="var(--mist)"/>
        <path d="M0,0 H520 C330,26 120,70 0,150 Z" fill="url(#corner-fill)"/>
      </g>
      <g class="corner corner--bottom" transform="rotate(180 318 450)">
        <path d="M0,0 H560 C360,30 130,80 0,170 Z" fill="var(--mist)"/>
        <path d="M0,0 H520 C330,26 120,70 0,150 Z" fill="url(#corner-fill)"/>
      </g>
    </svg>

    <div class="brand">
      <span class="brand__dot"></span>
      <span class="brand__name">
        <span class="brand__name-main">ALL SORTED</span>
        <span class="brand__name-sub">PROPERTY SERVICES</span>
      </span>
    </div>

    <address class="contact">
      <div>Your address, city</div>
      <div>state, ZIP 0000</div>
      <div class="contact__item">
        <svg class="contact__icon" viewBox="0 0 10 10"><path d="M2 0.5 L4 2.5 L3 4 Q4.5 6 6 7 L7.5 6 L9.5 8 L8 9.5 Q3 9 0.5 2 Z"/></svg>
        555-014-2100
      </div>
      <div class="contact__item">
        <svg class="contact__icon" viewBox="0 0 10 10"><rect x="0.5" y="2" width="9" height="6" rx="0.5"/><path d="M0.7 2.3 L5 5.5 L9.3 2.3" stroke="#fff" stroke-width="0.8" fill="none"/></svg>
        hello@allsorted.example
      </div>
      <div class="contact__item">
        <svg class="contact__icon" viewBox="0 0 10 10"><circle cx="5" cy="5" r="4.5"/><path d="M0.5 5 H9.5 M5 0.5 V9.5" stroke="#fff" stroke-width="0.7"/></svg>
        www.allsorted.example
      </div>
    </address>

    <article class="letter">
      <p class="letter__greeting">Dear Mr. Hale,</p>
      <p class="letter__para">Lorem ipsum dolor sit amet, consectetuer adipiscing elit, sed diam nonummy nibh euismod tincidunt ut laoreet dolore magna aliquam erat volutpat. Ut wisi enim ad minim veniam, quis nostrud exerci tation ullamcorper suscipit lobortis nisl ut aliquip ex ea commodo consequat. Duis autem vel eum iriure dolor in hendrerit in vulputate velit esse molestie consequat, vel illum dolore eu feugiat.</p>
      <p class="letter__para">Lorem ipsum dolor sit amet, consectetuer adipiscing elit, sed diam nonummy nibh euismod tincidunt ut laoreet dolore magna aliquam erat volutpat. Ut wisi enim ad minim veniam, quis nostrud exerci tation ullamcorper suscipit lobortis nisl ut aliquip ex ea commodo consequat. Duis autem vel eum iriure dolor in hendrerit in vulputate velit esse molestie.</p>
      <p class="letter__para">Lorem ipsum dolor sit amet, consectetuer adipiscing elit, sed diam nonummy nibh euismod tincidunt ut laoreet dolore magna aliquam erat volutpat. Ut wisi enim ad minim veniam, quis nostrud exerci tation ullamcorper suscipit lobortis nisl ut aliquip ex ea commodo consequat. Duis autem vel eum iriure dolor in hendrerit in vulputate velit esse molestie consequat, vel illum.</p>
      <p class="letter__para">Lorem ipsum dolor sit amet, consectetuer adipiscing elit, sed diam nonummy nibh euismod tincidunt ut laoreet dolore magna aliquam erat volutpat. Ut wisi enim ad minim veniam, quis nostrud exerci tation ullamcorper suscipit lobortis nisl ut aliquip ex ea commodo consequat.</p>
      <p class="letter__closing">Sincerely,</p>
      <div class="letter__signature" role="img" aria-label="Handwritten signature of the sender"></div>
    </article>
  </main>
</body>
</html>
```